Movie poster for indie thriller/film noir BITTER DOVES.

BITTER DOVES is a thriller about a gangster who forms an unlikely and dangerous friendship with his adulterous wife's former lover. This is a film noir with a romantic/dramatic edge to it, and is inspired by movies like RUN MALLOW, STONE FERRY and OLD WRENNA. Hero is a heartbroken criminal who's torn how to handle his wife's infidelity - he can't bear to kill or hurt her, but hurting people is all he knows. There are no big stars in the movie, so we don't want a poster showing the character's faces, but are looking more for something with an overall graphic concept. Open to ideas in this regard. Will upload some samples of older films/novels that have the feel to them we're after as well as some stills from the movie for inspiration. We like the idea of playing with light and shadow, but wouldn't go full black-and-white - might be better to rather keep a gritty, 70's texture. Our tag line is "FIND WHAT YOU LOVE. LET IT KILL YOU." Dimensions should be 27x40 - full-size movie poster for printing.
Target Market(s)
Audiences that like thrillers.
Industry/Entity Type
Movie
Colors
Designer to choose colors to be used in the design.
Requirements
Must have
- Placement for a credit block, title and our tagline "FIND WHAT YOU LOVE. LET IT KILL YOU."
Nice to have
- Element of danger/thriller. If possible hint at film's romantic edge.
Should not have
- Faces of our actors unless you find a really cool/interesting way to do it. Our actors aren't famous, so audiences will be more interested in a good graphic concept.

```html
<!DOCTYPE html>
<html lang="en">
<head>
<meta charset="utf-8">
<title>Bitter Doves — Poster</title>
<link rel="stylesheet" href="https://fonts.googleapis.com/css2?family=Montserrat:wght@800;900&family=Oswald:wght@600&display=swap">
<style>
  :root {
    --poster-warm: #c4622c;
    --poster-mid: #a8432b;
    --poster-deep: #84282a;
    --letter-light: #e8863a;
    --letter-dark: #c9662a;
    --letter-edge: #2a1208;
    --ink: #0d0705;
    --tagline: #b59a3e;
    --figure: #d9763a;
  }
  html, body {
    margin: 0;
    padding: 0;
    width: 916px;
    height: 1200px;
    overflow: hidden;
    background: var(--poster-deep);
  }
  .poster {
    display: block;
    width: 916px;
    height: 1200px;
  }
  .title-row {
    font-family: "Montserrat", sans-serif;
    font-weight: 900;
    font-size: 370px;
    fill: url(#letterFill);
    filter: url(#cutShadow);
  }
  .tagline {
    font-family: "Montserrat", sans-serif;
    font-weight: 800;
    font-size: 38px;
    fill: var(--tagline);
    letter-spacing: 2px;
  }
  .credit-block {
    font-family: "Oswald", sans-serif;
    font-weight: 600;
    font-size: 22px;
    fill: var(--ink);
  }
  .bullet { fill: var(--ink); }
  .figure { fill: var(--figure); opacity: 0.85; }
  .letter-art { fill: var(--ink); opacity: 0.35; }
</style>
</head>
<body>
<svg class="poster" viewBox="0 0 916 1200" xmlns="http://www.w3.org/2000/svg">
  <defs>
    <linearGradient id="bgFill" x1="0" y1="0" x2="1" y2="1">
      <stop offset="0" stop-color="var(--poster-warm)"/>
      <stop offset="0.55" stop-color="var(--poster-mid)"/>
      <stop offset="1" stop-color="var(--poster-deep)"/>
    </linearGradient>
    <radialGradient id="bgGlow" cx="0.3" cy="0.45" r="0.7">
      <stop offset="0" stop-color="#d4702f" stop-opacity="0.55"/>
      <stop offset="1" stop-color="#6e1f22" stop-opacity="0.35"/>
    </radialGradient>
    <linearGradient id="letterFill" x1="0" y1="0" x2="0" y2="1">
      <stop offset="0" stop-color="var(--letter-light)"/>
      <stop offset="1" stop-color="var(--letter-dark)"/>
    </linearGradient>
    <filter id="cutShadow" x="-5%" y="-5%" width="110%" height="110%">
      <feMorphology in="SourceAlpha" operator="dilate" radius="3" result="edge"/>
      <feOffset in="edge" dx="-4" dy="-5" result="edgeShift"/>
      <feFlood flood-color="#2a1208" flood-opacity="0.85"/>
      <feComposite in2="edgeShift" operator="in" result="edgeColor"/>
      <feGaussianBlur in="edgeColor" stdDeviation="2" result="edgeSoft"/>
      <feMerge>
        <feMergeNode in="edgeSoft"/>
        <feMergeNode in="SourceGraphic"/>
      </feMerge>
    </filter>
    <clipPath id="titleClip">
      <text x="21" y="275" font-family="Montserrat, sans-serif" font-weight="900" font-size="370" textLength="487" lengthAdjust="spacingAndGlyphs">BI</text>
      <text x="27" y="575" font-family="Montserrat, sans-serif" font-weight="900" font-size="370" textLength="593" lengthAdjust="spacingAndGlyphs">TTE</text>
      <text x="21" y="870" font-family="Montserrat, sans-serif" font-weight="900" font-size="370" textLength="728" lengthAdjust="spacingAndGlyphs">RDO</text>
      <text x="43" y="1175" font-family="Montserrat, sans-serif" font-weight="900" font-size="370" textLength="615" lengthAdjust="spacingAndGlyphs">VES</text>
    </clipPath>
  </defs>

  <rect class="background" width="916" height="1200" fill="url(#bgFill)"/>
  <rect class="background-glow" width="916" height="1200" fill="url(#bgGlow)"/>

  <g class="title">
    <text class="title-row" x="21" y="275" textLength="487" lengthAdjust="spacingAndGlyphs">BI</text>
    <text class="title-row" x="27" y="575" textLength="593" lengthAdjust="spacingAndGlyphs">TTE</text>
    <text class="title-row" x="21" y="870" textLength="728" lengthAdjust="spacingAndGlyphs">RDO</text>
    <text class="title-row" x="43" y="1175" textLength="615" lengthAdjust="spacingAndGlyphs">VES</text>
  </g>

  <g clip-path="url(#titleClip)">
    <rect class="letter-art" x="20" y="240" width="420" height="900" role="img" aria-label="Black handgun silhouettes seen through the title letters"/>
  </g>

  <rect class="bullet" x="570" y="90" width="50" height="112" rx="25" transform="rotate(-18 595 146)" role="img" aria-label="Bullet"/>
  <rect class="bullet" x="620" y="345" width="50" height="112" rx="25" transform="rotate(28 645 401)" role="img" aria-label="Bullet"/>
  <rect class="bullet" x="765" y="598" width="50" height="108" rx="25" transform="rotate(-30 790 652)" role="img" aria-label="Bullet"/>
  <rect class="bullet" x="750" y="882" width="50" height="112" rx="25" transform="rotate(12 775 938)" role="img" aria-label="Bullet"/>
  <rect class="bullet" x="418" y="1010" width="50" height="112" rx="25" transform="rotate(-14 443 1066)" role="img" aria-label="Bullet"/>

  <rect class="figure" x="688" y="62" width="58" height="212" rx="22" role="img" aria-label="Silhouette of a woman in a long dress"/>
  <rect class="figure" x="714" y="352" width="110" height="212" rx="20" role="img" aria-label="Silhouette of a man in a suit holding a gun"/>

  <text class="tagline" transform="translate(893 920) rotate(-90)" textLength="895" lengthAdjust="spacingAndGlyphs">FIND WHAT YOU LOVE. LET IT KILL YOU.</text>

  <g class="credit-block">
    <text x="738" y="1084">movie</text>
    <text x="738" y="1106">details</text>
    <text x="738" y="1128">here</text>
  </g>
</svg>
</body>
</html>
```